Silver Fern Counseling business cards

Dana Korvath, LCPC, NCC
(410)555-0187
www.silverferncounseling.example
dana@silverferncounseling.example

Business cards. I would like it on the same background as pictured. Not on a white business card. I have attached the logo that was done by another designer with artflockly. I am open to looking at single-sided and double-sided designs.

Target Market(s)

teenagers and adults

Industry/Entity Type

mental health

Contact Information for Business Card

Dana Korvath, LCPC, NCC (410)555-0187 dana@silverferncounseling.example

Font styles to use
Other font styles liked:
• Cinzel

Colors

Designer to choose colors to be used in the design.

Requirements
Must have
• logo that is attached

```html
<!DOCTYPE html>
<html lang="en">
<head>
<meta charset="utf-8">
<title>Silver Fern Counseling – Business Cards</title>
<link rel="stylesheet" href="https://fonts.googleapis.com/css2?family=Montserrat:wght@600;700&family=Poppins:wght@300;400&display=swap">
<style>
  :root {
    --navy: #04436a;
    --teal: #3a7891;
    --silver: #bdbdbd;
    --ink-grey: #6b6b6b;
    --white: #ffffff;
    --backdrop: #e9e7e3;
  }
  * { box-sizing: border-box; margin: 0; padding: 0; }
  html, body { width: 1200px; height: 900px; overflow: hidden; }
  body {
    background: var(--backdrop);
    font-family: "Poppins", Arial, sans-serif;
    position: relative;
  }
  .card {
    position: absolute;
    left: 270px;
    width: 660px;
    height: 377px;
    overflow: hidden;
    box-shadow: 0 6px 18px rgba(0,0,0,0.18);
  }
  .card--front { top: 60px; background: var(--navy); }
  .card--back { top: 463px; background: var(--white); }

  .brand {
    display: flex;
    align-items: center;
    gap: 14px;
    font-family: "Montserrat", Arial, sans-serif;
    font-weight: 700;
    text-transform: uppercase;
    letter-spacing: 1px;
    line-height: 1.1;
  }
  .brand__dot { border-radius: 50%; flex: none; }

  .card--front .brand {
    position: absolute;
    left: 0; right: 0; top: 0; bottom: 0;
    flex-direction: column;
    justify-content: center;
    color: var(--white);
    font-size: 34px;
    text-align: center;
  }
  .card--front .brand__dot { width: 74px; height: 74px; background: var(--silver); }

  .holder {
    position: absolute;
    left: 40px; top: 84px;
    font-family: "Montserrat", Arial, sans-serif;
    font-weight: 700;
    color: var(--navy);
    font-size: 25px;
    letter-spacing: 0.5px;
    text-transform: uppercase;
  }
  .holder__credentials { font-size: 14px; }

  .card--back .brand {
    position: absolute;
    right: 34px; top: 36px;
    width: 210px;
    flex-direction: column;
    color: var(--navy);
    font-size: 22px;
    text-align: center;
  }
  .card--back .brand__dot { width: 56px; height: 56px; background: var(--teal); }

  .contact {
    position: absolute;
    left: 40px; top: 172px;
    list-style: none;
    color: var(--ink-grey);
    font-weight: 300;
    font-size: 17px;
  }
  .contact__item { display: flex; align-items: center; gap: 12px; margin-bottom: 6px; }
  .contact__icon { width: 20px; height: 20px; fill: var(--navy); flex: none; }

  .wave { position: absolute; left: 0; top: 0; width: 660px; height: 377px; }
  .website {
    position: absolute;
    right: 28px; bottom: 22px;
    color: var(--white);
    font-size: 16px;
    letter-spacing: 0.3px;
  }
</style>
</head>
<body>

<section class="card card--front" aria-label="Card front">
  <div class="brand">
    <span class="brand__dot"></span>
    <span class="brand__name">Silver Fern<br>Counseling</span>
  </div>
</section>

<section class="card card--back" aria-label="Card back">
  <svg class="wave" viewBox="0 0 660 377" aria-hidden="true">
    <path d="M0 300 C260 312 470 262 660 164 L660 377 L0 377 Z" fill="var(--silver)"/>
    <path d="M0 306 C260 318 470 270 660 176 L660 377 L0 377 Z" fill="var(--white)"/>
    <path d="M0 311 C260 323 475 275 660 184 L660 377 L0 377 Z" fill="var(--teal)"/>
    <path d="M0 332 C270 342 480 284 660 188 L660 377 L0 377 Z" fill="var(--white)"/>
    <path d="M0 337 C270 347 482 288 660 192 L660 377 L0 377 Z" fill="var(--navy)"/>
  </svg>

  <h1 class="holder">Dana Korvath, <span class="holder__credentials">LCPC, NCC</span></h1>

  <div class="brand">
    <span class="brand__dot"></span>
    <span class="brand__name">Silver Fern<br>Counseling</span>
  </div>

  <ul class="contact">
    <li class="contact__item">
      <svg class="contact__icon" viewBox="0 0 24 24" aria-hidden="true"><path d="M6.6 10.8a15.1 15.1 0 0 0 6.6 6.6l2.2-2.2a1 1 0 0 1 1-.25 11.4 11.4 0 0 0 3.6.57 1 1 0 0 1 1 1V20a1 1 0 0 1-1 1A17 17 0 0 1 3 4a1 1 0 0 1 1-1h3.5a1 1 0 0 1 1 1c0 1.25.2 2.45.57 3.57a1 1 0 0 1-.25 1z"/></svg>
      <span>(410)555-0187</span>
    </li>
    <li class="contact__item">
      <svg class="contact__icon" viewBox="0 0 24 24" aria-hidden="true"><path d="M2 5h20v14H2z M4 7v.5l8 5.5 8-5.5V7z" fill-rule="evenodd"/></svg>
      <span>dana@silverferncounseling.example</span>
    </li>
  </ul>

  <p class="website">www.silverferncounseling.example</p>
</section>

</body>
</html>
```